Website for Outdoor Furniture, Sunroom and life style design

I need a website for a company that creates sunroom furniture and design. A sunroom is a room within your home that is surrounded by windows to make it feel like you are outdoors while being indoors to protect you from weather and keep your comfortable.<br/><br/>The company designs and decorates sun rooms for home owners who want to relax and have the feeling of outdoors, while being indoors.

Target Market(s)

home owners, 40+ demographic

Number of Pages Required

5+ page

Requirements
Must have
• See attached zip files for more information including images, copy and descriptions.
• **CONTACT ONLY FROM PIXELBAZAR.COM ALL OTHER FORMS OF COMMUNICATION WILL BE IGNORED**
• COLORS: colors that compliment our logo which is attached here
• Clean, streamlined, easy to navigate.
• No clutter, flashing, bouncing, pop ups.
• Contact info on every page - phone, email, address, hours. the Map somewhere.
• Videos on every page relevant to the content
• Our products are sunrooms and shade but we consider ourselves to be selling a lifestyle. Outdoor living and design.
• Would like to incorporate images of people in our 40 plus demographic to reinforce the lifestyle theme.
• We need the following pages designed (Please see attached zip file for images and sample copy)
• 1. Home: Home page to have prominent area for updating current info like holiday hours, sales, new products, etc
• 2. Sunrooms: See attached zip file for images, text copy etc....
• 3. Shade Solutions: See attached zip file for images, text copy etc....
• 4. Options & Accessories: See attached zip file for images, text copy etc....
• 5. About Us: See attached zip file for images, text copy etc....
• Customer comments/reviews to appear in “bubbles” throughout site
Should not have
• - No search bar
• - No clutter, flashing, bouncing, pop ups.

```html
<!DOCTYPE html>
<html lang="en">
<head>
<meta charset="utf-8">
<title>Shade Solutions – Brightway Rooms</title>
<link href="https://fonts.googleapis.com/css2?family=Libre+Baskerville:wght@700&family=Open+Sans:wght@400&family=Roboto:wght@400&family=Lato:wght@400&display=swap" rel="stylesheet">
<style>
:root{
  --hero-bg:#eef1f4;
  --ink:#1a1a1a;
  --brand-ink:#333;
  --orange:#d8601f;
  --gold:#e39a2c;
  --grey-text:#666;
  --band:#f3f3f3;
  --footer-bar:#2b2b2b;
}
*{margin:0;padding:0;box-sizing:border-box}
html,body{width:825px;height:1200px;overflow:hidden;background:#fff}
body{position:relative;font-family:'Open Sans',sans-serif;color:var(--ink)}
.abs{position:absolute}
.hero{left:0;top:0;width:825px;height:254px;background:var(--hero-bg)}
.brand{font-family:'Open Sans',sans-serif;font-weight:400;color:var(--brand-ink);font-size:15px;line-height:1;display:flex;align-items:center;gap:7px}
.brand .mark{width:12px;height:12px;background:var(--brand-ink)}
.nav{top:25px;font-family:'Roboto',sans-serif;font-size:10px;color:#444;white-space:nowrap}
.nav.light{color:#fff}
.nav.active::after{content:"";position:absolute;left:19px;right:12px;top:16px;height:1.5px;background:var(--orange)}
.call{left:754px;top:19px;width:23px;height:23px;background:#fff;display:flex;align-items:center;justify-content:center}
.hero-title{left:90px;top:128px;font-family:'Libre Baskerville',serif;font-weight:700;font-size:32px;color:var(--gold)}
.section-title{left:0;width:825px;top:299px;line-height:26px;text-align:center;font-family:'Libre Baskerville',serif;font-weight:700;font-size:23px}
.rule{left:361px;width:110px;height:1.5px;background:var(--orange)}
.intro{left:114px;width:600px;top:342px;text-align:center;font-size:12.5px;line-height:20px;color:var(--grey-text)}
.card{width:158px;top:521px}
.card .photo{width:158px;height:116px}
.card h3{margin-top:14px;font-family:'Libre Baskerville',serif;font-weight:700;font-size:12.5px;line-height:16.5px;color:#222}
.card p{margin-top:12px;font-size:10px;line-height:17px;color:var(--grey-text)}
.foot-brand{left:0;width:825px;top:852px;display:flex;justify-content:center}
.foot-nav{left:0;width:825px;top:906px;display:flex;justify-content:center;gap:21px;font-family:'Lato',sans-serif;font-size:9px;color:#333}
.foot-line{left:99px;width:636px;top:932px;height:1px;background:#ccc}
.col{top:958px;font-family:'Lato',sans-serif;font-size:9px;color:#444}
.col h4{font-family:'Libre Baskerville',serif;font-weight:700;font-size:10.5px;color:#444;margin-bottom:12px}
.col li{list-style:none;line-height:17.6px}
.contact li{display:flex;align-items:center;gap:7px;line-height:31px}
.map-btn{left:322px;top:1099px;width:154px;height:36px;border:1.5px solid var(--orange);display:flex;align-items:center;justify-content:center;font-family:'Libre Baskerville',serif;font-weight:700;font-size:10px;color:var(--orange)}
.bar{left:0;top:1151px;width:825px;height:49px;background:var(--footer-bar);color:#ddd;font-family:'Lato',sans-serif;font-size:9px;display:flex;justify-content:center;align-items:center}
</style>
</head>
<body>

<div class="abs hero"></div>
<svg class="abs" style="left:0;top:0" width="825" height="254" role="img" aria-label="Photo of a white patio cover over a garden deck with flowers">
  <defs><linearGradient id="g1" x1="0" y1="0" x2="1" y2="1"><stop offset="0" stop-color="#c9cfcc"/><stop offset=".4" stop-color="#5f7a45"/><stop offset="1" stop-color="#3e4a36"/></linearGradient></defs>
  <polygon points="583,0 825,0 825,254 405,254" fill="url(#g1)"/>
</svg>

<div class="abs brand" style="left:95px;top:22px"><span class="mark"></span>Brightway Rooms</div>

<span class="abs nav" style="left:271px">Home</span>
<span class="abs nav" style="left:315px">Sunrooms</span>
<span class="abs nav active" style="left:378px">Shade Solutions</span>
<span class="abs nav" style="left:469px">Options &amp; Accessories</span>
<span class="abs nav light" style="left:589px">About Us</span>
<span class="abs nav light" style="left:647px">FAQs</span>
<span class="abs nav light" style="left:687px">Contact Us</span>
<div class="abs call"><svg width="12" height="12" viewBox="0 0 24 24"><path fill="var(--orange)" d="M6.6 10.8a15 15 0 0 0 6.6 6.6l2.2-2.2c.3-.3.7-.4 1-.2 1.1.4 2.3.6 3.6.6.6 0 1 .4 1 1V20c0 .6-.4 1-1 1A17 17 0 0 1 3 4c0-.6.4-1 1-1h3.5c.6 0 1 .4 1 1 0 1.3.2 2.5.6 3.6.1.3 0 .7-.2 1z"/></svg></div>

<h1 class="abs hero-title">Shade Solution</h1>

<div class="abs rule" style="top:294px"></div>
<h2 class="abs section-title">Shade Solutions</h2>
<div class="abs rule" style="top:328px"></div>
<p class="abs intro">Are you getting all of the enjoyment you can from your deck or patio or is it just too hot for you to sit out?If you need some shade, then we have the shade solution that's perfect for you!</p>

<svg class="abs" style="left:0;top:420px" width="825" height="420">
  <defs>
    <linearGradient id="og" x1="0" x2="1"><stop offset="0" stop-color="#cc4b17"/><stop offset="1" stop-color="#e88a2a"/></linearGradient>
    <linearGradient id="yg" x1="0" x2="1"><stop offset="0" stop-color="#e0931c"/><stop offset="1" stop-color="#ebb43a"/></linearGradient>
  </defs>
  <polygon points="0,50 825,13 825,366 0,403" fill="var(--band)"/>
  <polygon points="0,3 440,30 0,50" fill="url(#og)"/>
  <polygon points="390,386 825,366 825,413" fill="url(#yg)"/>
</svg>

<div class="abs card" style="left:62px">
  <div class="photo" role="img" aria-label="Acrylic patio cover over a dining set beside a brick house" style="background:linear-gradient(135deg,#8a4a35,#6d7d4e)"></div>
  <h3>Clearview Acrylice Patio Covers</h3>
  <p>Aget arcurmentum vel congue id euismod in elit Fusce ultricies orci ac feugiat suscipit leo</p>
</div>
<div class="abs card" style="left:239px">
  <div class="photo" role="img" aria-label="Insulated patio cover over a wooden deck with plants" style="background:linear-gradient(180deg,#6fa8d8,#b7a47a 60%,#6f9a3e)"></div>
  <h3>CoolCap Isulated Patio Covers</h3>
  <p>Aget arcurmentum vel congue id euismod in elit Fusce ultricies orci ac feugiat suscipit leo</p>
</div>
<div class="abs card" style="left:420px">
  <div class="photo" role="img" aria-label="Louvered roof pergola in a green garden" style="background:linear-gradient(180deg,#d9dcd8,#4c6a38 50%,#7b7668)"></div>
  <h3>Louvered<br>Roof</h3>
  <p>Aget arcurmentum vel congue id euismod in elit Fusce ultricies orci ac feugiat suscipit leo</p>
</div>
<div class="abs card" style="left:597px">
  <div class="photo" role="img" aria-label="Yellow retractable awning over a patio" style="background:linear-gradient(160deg,#f2b21e,#d29a3a 55%,#4f6e3a)"></div>
  <h3>Retraetable<br>Awnings</h3>
  <p>Aget arcurmentum vel congue id euismod in elit Fusce ultricies orci ac feugiat suscipit leo</p>
</div>

<div class="abs foot-brand"><div class="brand"><span class="mark"></span>Brightway Rooms</div></div>

<nav class="abs foot-nav">
  <span>Home</span><span>Sunrooms</span><span>Shade Solutions</span><span>Options &amp; Accessories</span><span>About Us</span><span>FAQs</span><span>Contact Us</span>
</nav>
<div class="abs foot-line"></div>

<div class="abs col" style="left:101px">
  <h4>Sunrooms</h4>
  <ul><li>Sunroom Generals</li><li>3 Season Vinyl Four Track</li><li>3 Season Single Glazed Glass</li><li>All Season Thermal Sunroom</li><li>Recreational Vehicals</li><li>Fill Ins</li></ul>
</div>
<div class="abs col" style="left:274px">
  <h4>Shade Solutions</h4>
  <ul><li>Shade Solutions</li><li>Clearview Acrulic Patio</li><li>CoolCap Insulated</li><li>Louvered Roof</li><li>Rectactable Awnings</li></ul>
</div>
<div class="abs col" style="left:429px">
  <h4>Products</h4>
  <ul><li>Flooring Covering</li><li>Floor System</li><li>Medical Piers</li><li>Ralings</li><li>Sunsades</li></ul>
</div>
<div class="abs col contact" style="left:583px">
  <h4>Contact info</h4>
  <ul>
    <li><svg width="11" height="11" viewBox="0 0 24 24"><path fill="var(--gold)" d="M6.6 10.8a15 15 0 0 0 6.6 6.6l2.2-2.2c.3-.3.7-.4 1-.2 1.1.4 2.3.6 3.6.6.6 0 1 .4 1 1V20c0 .6-.4 1-1 1A17 17 0 0 1 3 4c0-.6.4-1 1-1h3.5c.6 0 1 .4 1 1 0 1.3.2 2.5.6 3.6.1.3 0 .7-.2 1z"/></svg>905 555 0142</li>
    <li><svg width="11" height="9" viewBox="0 0 24 18"><rect width="24" height="18" fill="var(--gold)"/><path d="M0 0l12 9 12-9" stroke="#fff" stroke-width="2" fill="none"/></svg>info@brightwayrooms.com</li>
    <li><svg width="11" height="12" viewBox="0 0 24 28"><path fill="var(--gold)" d="M12 0a10 10 0 0 0-10 10c0 7 10 18 10 18s10-11 10-18A10 10 0 0 0 12 0zm0 14a4 4 0 1 1 0-8 4 4 0 0 1 0 8z"/></svg>14 Maple Ave. Fenwick, Ontario</li>
  </ul>
</div>

<div class="abs map-btn">View us on the Map</div>

<footer class="abs bar">© 2020 Company Name &nbsp;|&nbsp; All Rights Reserved &nbsp;|&nbsp; Disclaimer</footer>

</body>
</html>
```